Review/Re-Design Supermarket E-Commerce website

We have launched our Supermarket E-commerce Website but feel it is lacking a modern feel.

Please re-design the current Supermarket E-commerce site, creating a more modern look and feel.

I am looking for design changes to things such as:

- Fonts
- Button shape & Size
- Shapes of boxes
- Layout of drop down menus
- A new shopping cart / button
- The Header (and in particular the use and positioning of the logo)
- Supplying a generic background image (currently berries)

Please do not change the structure of the page. For instance, the category selection will always be on the left, the items will always be displayed in rows of 3 and the shopping cart should be on the right.
Updates

Current site can be found at www.brovanmarket.com.au

Project Deadline Extended
Reason: designs coming in are generally too different from current design. we are looking for less that 10% change to the overall look and feel. one aspect that needs a lot of work is the checkout cart on the right hand side. please checkout http://www2.pelkinfreshmart.com.au/?gclid=QXRP4kdmwnLBHTYEzJuaPGEKtB

Target Market(s)

Consumers buying their weekly grocery shopping online

Industry/Entity Type

Shopping

Number of Pages Required

1 page

Requirements
Must have
• Stick to the branding of the Logo. Which is Red, Blue and White.
• Other colours may be used in small percentages.
Should not have
• Do not change the Structure of the site.

```html
<!DOCTYPE html>
<html lang="en">
<head>
<meta charset="utf-8">
<title>Brovan Market – Apples</title>
<link href="https://fonts.googleapis.com/css2?family=Open+Sans:wght@300;400;600;700&family=Raleway:wght@700&display=swap" rel="stylesheet">
<style>
:root{
  --red:#ee1b2e;
  --blue:#0a63ae;
  --green-dark:#1e5c2e;
  --cyan:#1aa6d6;
  --lime:#9cc11f;
  --band:#c5d3d6;
  --crumb:#e9eef5;
  --ink:#222;
  --muted:#d5d5d5;
  --line:#c9c9c9;
  --white:#fff;
}
*{box-sizing:border-box;margin:0;padding:0}
html,body{width:1200px;height:1000px;overflow:hidden;background:var(--white);font-family:"Open Sans",sans-serif;color:var(--ink)}
.topbar{position:absolute;left:0;top:0;width:1200px;height:40px;background:var(--red);color:var(--white)}
.contact{position:absolute;left:168px;top:6px;height:28px;width:222px;border:1.5px solid var(--white);border-radius:14px;display:flex;align-items:center;padding-left:10px;gap:12px}
.contact .label{font-size:12px;font-weight:700}
.contact .phone{font-size:17px;font-weight:700;display:flex;align-items:center;gap:6px}
.topnav{position:absolute;right:95px;top:0;height:40px;display:flex;align-items:center;gap:14px;font-size:11px;font-weight:600}
.topnav .item{display:flex;align-items:center;gap:7px}
.cart-count{background:var(--white);color:var(--ink);border-radius:10px;padding:1px 12px;font-size:13px;font-weight:700}
.cart-count i{font-weight:400;font-size:11px}
.header{position:absolute;left:0;top:40px;width:1200px;height:60px;background:var(--white);box-shadow:0 2px 3px rgba(0,0,0,.35);z-index:2}
.brand{position:absolute;left:168px;top:16px;display:flex;align-items:center;gap:8px;font-size:20px;font-weight:700;color:var(--blue);letter-spacing:.5px}
.brand .mark{width:20px;height:20px;background:var(--red);border-radius:50%}
.search{position:absolute;left:520px;top:14px;width:256px;height:35px;border:2px solid var(--green-dark);border-radius:5px;padding-left:11px;font-size:13px;color:#ccc;display:flex;align-items:center;font-weight:300}
.search-btn{position:absolute;left:779px;top:14px;width:60px;height:35px;background:var(--blue);border-radius:5px;display:flex;align-items:center;justify-content:center}
.dropdown{position:absolute;top:15px;width:121px;height:33px;border:1px solid var(--green-dark);border-radius:5px;font-size:14px;display:flex;align-items:center;justify-content:space-between;padding:0 10px 0 17px;color:#333}
.crumbs{position:absolute;left:0;top:101px;width:1200px;height:29px;background:var(--crumb);font-size:9px;display:flex;align-items:center;padding-left:168px;gap:6px}
.crumbs b{font-weight:700}
.card{position:absolute;width:231px}
.notice{height:18px;background:var(--lime);border-radius:4px;font-size:8px;display:flex;align-items:center;justify-content:space-between;padding:0 10px 0 4px}
.box{margin-top:8px;height:272px;border:1px solid var(--line);border-radius:5px;overflow:hidden}
.photo{height:161px;display:flex;align-items:center;justify-content:center}
.photo div{width:128px;height:124px;border-radius:46%;background:radial-gradient(circle at 45% 40%,#e0374a,#b5101e 70%,#9a0c18)}
.name{height:26px;background:var(--band);text-align:center;font-size:15px;line-height:26px}
.name b{color:var(--red);font-weight:700}
.price-row{position:relative;height:49px;margin:0 9px;border-bottom:1px solid var(--line)}
.price{position:absolute;left:8px;top:12px;font-size:19px;font-weight:300}
.price span{color:var(--muted)}
.qty{position:absolute;right:0;top:12px;width:34px;height:25px;border:1px solid #aaa;font-size:13px;text-align:center;line-height:23px}
.actions{display:flex;align-items:center;padding:5px 0 0 17px;gap:9px}
.add{width:90px;height:23px;background:var(--cyan);border-radius:3px;color:var(--white);font-family:"Raleway",sans-serif;font-weight:700;font-size:10px;display:flex;align-items:center;justify-content:center;gap:5px}
.sep{width:1px;height:20px;background:#ddd}
.details{font-family:"Raleway",sans-serif;font-weight:700;font-size:10px;display:flex;align-items:center;gap:5px}
.sidebar{position:absolute;left:892px;top:146px;width:217px;height:844px;background:#fafafa;border-radius:4px;box-shadow:0 1px 3px rgba(0,0,0,.35)}
.fav{margin:0 16px;height:45px;border-bottom:1px solid #e6e6e6;display:flex;align-items:center;gap:14px;padding-left:24px;font-size:12px;font-weight:600;color:#666}
</style>
</head>
<body>
<div class="topbar">
  <div class="contact"><span class="label">Contact us</span><span class="phone">
    <svg width="11" height="18" viewBox="0 0 11 18"><rect x="1" y="1" width="9" height="16" rx="2" fill="none" stroke="#fff" stroke-width="2"/><rect x="4" y="13" width="3" height="2" fill="#fff"/></svg>1300 555 210</span></div>
  <nav class="topnav">
    <span class="item">PRODUCTS</span>
    <span class="item"><svg width="16" height="14" viewBox="0 0 16 14"><path d="M0 1h3l2 8h9l2-6H4" fill="#fff"/><circle cx="6" cy="12" r="1.6" fill="#fff"/><circle cx="13" cy="12" r="1.6" fill="#fff"/></svg>MYCART <span class="cart-count">12 <i>items</i></span></span>
    <span class="item"><svg width="12" height="13" viewBox="0 0 12 13"><circle cx="6" cy="3.5" r="3.2" fill="#fff"/><path d="M0 13c0-4 2.5-6 6-6s6 2 6 6z" fill="#fff"/></svg>&nbsp;LOGIN</span>
    <span class="item"><svg width="11" height="13" viewBox="0 0 11 13"><path d="M2.5 6V4a3 3 0 0 1 6 0v2" stroke="#fff" stroke-width="2" fill="none"/><rect x="0" y="6" width="11" height="7" rx="1" fill="#fff"/></svg>&nbsp;REGISTER</span>
  </nav>
</div>

<header class="header">
  <div class="brand"><span>BROVAN MARKET</span><span class="mark"></span></div>
  <div class="search">Search Product...........</div>
  <div class="search-btn"><svg width="22" height="22" viewBox="0 0 22 22"><circle cx="9" cy="9" r="7" stroke="#fff" stroke-width="3" fill="none"/><path d="M14 14l6 6" stroke="#fff" stroke-width="3.5" stroke-linecap="round"/></svg></div>
  <div class="dropdown" style="left:852px">Filter By<svg width="20" height="11" viewBox="0 0 20 11"><path d="M0 0h20L10 11z" fill="#111"/></svg></div>
  <div class="dropdown" style="left:987px">Sort By<svg width="20" height="11" viewBox="0 0 20 11"><path d="M0 0h20L10 11z" fill="#111"/></svg></div>
</header>

<div class="crumbs">HOME <span>/</span> FRUITS <span>/</span> <b>APPLES</b></div>

<main>
  <!-- product cards -->
  <article class="card" style="left:168px;top:146px">
    <div class="notice"><svg width="12" height="12" viewBox="0 0 12 12"><circle cx="6" cy="6" r="5" fill="none" stroke="#fff" stroke-width="1.3"/><path d="M3.5 6l2 2 3-3.5" stroke="#fff" stroke-width="1.3" fill="none"/></svg>Successfully Added to Cart</div>
    <div class="box">
      <div class="photo"><div role="img" aria-label="Bag of red apples"></div></div>
      <div class="name"><b>RED APPLE</b> 2KG BAG</div>
      <div class="price-row"><span class="price">$8.39 - <span>$8.39 ea</span></span><span class="qty">1</span></div>
      <div class="actions"><span class="add"><svg width="14" height="11" viewBox="0 0 16 14"><path d="M0 1h3l2 8h9l2-6H4" fill="#fff"/><circle cx="6" cy="12" r="1.6" fill="#fff"/><circle cx="13" cy="12" r="1.6" fill="#fff"/></svg>Add to Cart</span><span class="sep"></span><span class="details"><svg width="26" height="20" viewBox="0 0 26 20"><rect x="1" y="1" width="24" height="18" rx="2" fill="none" stroke="#111" stroke-width="2"/><path d="M5 6h2M9 6h12M5 10h2M9 10h12M5 14h2M9 14h12" stroke="#111" stroke-width="2"/></svg>More Details</span></div>
    </div>
  </article>
  <article class="card" style="left:407px;top:146px">
    <div class="notice"><svg width="12" height="12" viewBox="0 0 12 12"><circle cx="6" cy="6" r="5" fill="none" stroke="#fff" stroke-width="1.3"/><path d="M3.5 6l2 2 3-3.5" stroke="#fff" stroke-width="1.3" fill="none"/></svg>Successfully Added to Cart</div>
    <div class="box">
      <div class="photo"><div role="img" aria-label="Bag of red apples"></div></div>
      <div class="name"><b>RED APPLE</b> 2KG BAG</div>
      <div class="price-row"><span class="price">$8.39 - <span>$8.39 ea</span></span><span class="qty">1</span></div>
      <div class="actions"><span class="add"><svg width="14" height="11" viewBox="0 0 16 14"><path d="M0 1h3l2 8h9l2-6H4" fill="#fff"/><circle cx="6" cy="12" r="1.6" fill="#fff"/><circle cx="13" cy="12" r="1.6" fill="#fff"/></svg>Add to Cart</span><span class="sep"></span><span class="details"><svg width="26" height="20" viewBox="0 0 26 20"><rect x="1" y="1" width="24" height="18" rx="2" fill="none" stroke="#111" stroke-width="2"/><path d="M5 6h2M9 6h12M5 10h2M9 10h12M5 14h2M9 14h12" stroke="#111" stroke-width="2"/></svg>More Details</span></div>
    </div>
  </article>
  <article class="card" style="left:647px;top:146px">
    <div class="notice"><svg width="12" height="12" viewBox="0 0 12 12"><circle cx="6" cy="6" r="5" fill="none" stroke="#fff" stroke-width="1.3"/><path d="M3.5 6l2 2 3-3.5" stroke="#fff" stroke-width="1.3" fill="none"/></svg>Successfully Added to Cart</div>
    <div class="box">
      <div class="photo"><div role="img" aria-label="Bag of red apples"></div></div>
      <div class="name"><b>RED APPLE</b> 2KG BAG</div>
      <div class="price-row"><span class="price">$8.39 - <span>$8.39 ea</span></span><span class="qty">1</span></div>
      <div class="actions"><span class="add"><svg width="14" height="11" viewBox="0 0 16 14"><path d="M0 1h3l2 8h9l2-6H4" fill="#fff"/><circle cx="6" cy="12" r="1.6" fill="#fff"/><circle cx="13" cy="12" r="1.6" fill="#fff"/></svg>Add to Cart</span><span class="sep"></span><span class="details"><svg width="26" height="20" viewBox="0 0 26 20"><rect x="1" y="1" width="24" height="18" rx="2" fill="none" stroke="#111" stroke-width="2"/><path d="M5 6h2M9 6h12M5 10h2M9 10h12M5 14h2M9 14h12" stroke="#111" stroke-width="2"/></svg>More Details</span></div>
    </div>
  </article>
  <article class="card" style="left:166px;top:466px">
    <div class="notice"><svg width="12" height="12" viewBox="0 0 12 12"><circle cx="6" cy="6" r="5" fill="none" stroke="#fff" stroke-width="1.3"/><path d="M3.5 6l2 2 3-3.5" stroke="#fff" stroke-width="1.3" fill="none"/></svg>Successfully Added to Cart</div>
    <div class="box">
      <div class="photo"><div role="img" aria-label="Bag of red apples"></div></div>
      <div class="name"><b>RED APPLE</b> 2KG BAG</div>
      <div class="price-row"><span class="price">$8.39 - <span>$8.39 ea</span></span><span class="qty">1</span></div>
      <div class="actions"><span class="add"><svg width="14" height="11" viewBox="0 0 16 14"><path d="M0 1h3l2 8h9l2-6H4" fill="#fff"/><circle cx="6" cy="12" r="1.6" fill="#fff"/><circle cx="13" cy="12" r="1.6" fill="#fff"/></svg>Add to Cart</span><span class="sep"></span><span class="details"><svg width="26" height="20" viewBox="0 0 26 20"><rect x="1" y="1" width="24" height="18" rx="2" fill="none" stroke="#111" stroke-width="2"/><path d="M5 6h2M9 6h12M5 10h2M9 10h12M5 14h2M9 14h12" stroke="#111" stroke-width="2"/></svg>More Details</span></div>
    </div>
  </article>
  <article class="card" style="left:405px;top:466px">
    <div class="notice"><svg width="12" height="12" viewBox="0 0 12 12"><circle cx="6" cy="6" r="5" fill="none" stroke="#fff" stroke-width="1.3"/><path d="M3.5 6l2 2 3-3.5" stroke="#fff" stroke-width="1.3" fill="none"/></svg>Successfully Added to Cart</div>
    <div class="box">
      <div class="photo"><div role="img" aria-label="Bag of red apples"></div></div>
      <div class="name"><b>RED APPLE</b> 2KG BAG</div>
      <div class="price-row"><span class="price">$8.39 - <span>$8.39 ea</span></span><span class="qty">1</span></div>
      <div class="actions"><span class="add"><svg width="14" height="11" viewBox="0 0 16 14"><path d="M0 1h3l2 8h9l2-6H4" fill="#fff"/><circle cx="6" cy="12" r="1.6" fill="#fff"/><circle cx="13" cy="12" r="1.6" fill="#fff"/></svg>Add to Cart</span><span class="sep"></span><span class="details"><svg width="26" height="20" viewBox="0 0 26 20"><rect x="1" y="1" width="24" height="18" rx="2" fill="none" stroke="#111" stroke-width="2"/><path d="M5 6h2M9 6h12M5 10h2M9 10h12M5 14h2M9 14h12" stroke="#111" stroke-width="2"/></svg>More Details</span></div>
    </div>
  </article>
  <article class="card" style="left:645px;top:466px">
    <div class="notice"><svg width="12" height="12" viewBox="0 0 12 12"><circle cx="6" cy="6" r="5" fill="none" stroke="#fff" stroke-width="1.3"/><path d="M3.5 6l2 2 3-3.5" stroke="#fff" stroke-width="1.3" fill="none"/></svg>Successfully Added to Cart</div>
    <div class="box">
      <div class="photo"><div role="img" aria-label="Bag of red apples"></div></div>
      <div class="name"><b>RED APPLE</b> 2KG BAG</div>
      <div class="price-row"><span class="price">$8.39 - <span>$8.39 ea</span></span><span class="qty">1</span></div>
      <div class="actions"><span class="add"><svg width="14" height="11" viewBox="0 0 16 14"><path d="M0 1h3l2 8h9l2-6H4" fill="#fff"/><circle cx="6" cy="12" r="1.6" fill="#fff"/><circle cx="13" cy="12" r="1.6" fill="#fff"/></svg>Add to Cart</span><span class="sep"></span><span class="details"><svg width="26" height="20" viewBox="0 0 26 20"><rect x="1" y="1" width="24" height="18" rx="2" fill="none" stroke="#111" stroke-width="2"/><path d="M5 6h2M9 6h12M5 10h2M9 10h12M5 14h2M9 14h12" stroke="#111" stroke-width="2"/></svg>More Details</span></div>
    </div>
  </article>
</main>

<aside class="sidebar">
  <div class="fav"><svg width="30" height="30" viewBox="0 0 30 30"><path d="M15 1l3.5 9 9.5-1-7 7 6 9-9-3-3 8-3-8-9 3 6-9-7-7 9.5 1z" fill="#f2c80f"/></svg>Favourits</div>
</aside>
</body>
</html>
```